Outdoor kitchen and Appliance Need new business card

We need a new business card, for our business.

Front side with all info, back side with more brand identity.

I have attached some drafts, we moved up but it lacks creativity.

Use https://photos.quendrix.com and I can purchase, the stock photo and send it you if you design is chosen.

We are also planing on printing business card with the logo, having a spot uv. I have attached instructions.

Plumtarvessa.com is our website

Target Market(s)

Extremely high end customer.

Contact Information for Business Card

Double sided with spot uv on logos

Colors
ec1f27

Requirements
Must have
• See sample I have attached, we are open to ideas.

Colors, are: RED, Stainless steel, Black

```html
<!DOCTYPE html>
<html lang="en">
<head>
<meta charset="utf-8">
<title>Plumtarvessa – Business Card</title>
<link rel="stylesheet" href="https://fonts.googleapis.com/css2?family=Arvo:wght@700&family=Arimo:wght@400;700&display=swap">
<style>
  :root {
    --bg: #2b2b2d;
    --card-black: #0d0d0e;
    --brand-red: #ec1f27;
    --deep-red: #d9000d;
    --steel: #c9cacd;
    --steel-dark: #9a9ca0;
    --gloss: #2a2a2c;
    --white: #ffffff;
  }
  * { box-sizing: border-box; margin: 0; padding: 0; }
  html, body { width: 1200px; height: 1015px; overflow: hidden; }
  body {
    background: var(--bg);
    display: flex;
    flex-direction: column;
    align-items: center;
    justify-content: center;
    gap: 60px;
    font-family: "Arimo", Arial, sans-serif;
  }
  .card {
    position: relative;
    width: 700px;
    height: 400px;
    background: var(--card-black);
    overflow: hidden;
    box-shadow: 0 10px 30px rgba(0,0,0,.5);
  }
  .brand-mark {
    position: absolute;
    display: flex;
    align-items: center;
    gap: 14px;
    font-family: "Arvo", Georgia, serif;
    font-weight: 700;
    white-space: nowrap;
  }
  .brand-dot { width: 26px; height: 26px; border-radius: 50%; }
  .card--back .brand-mark {
    left: 50%; top: 50%;
    transform: translate(-50%, -50%);
    font-size: 46px;
    color: var(--gloss);
  }
  .card--back .brand-dot { background: var(--gloss); }
  .card--front .brand-mark {
    left: 50px; top: 128px;
    font-size: 32px;
    color: var(--steel);
  }
  .card--front .brand-dot { background: var(--steel); width: 20px; height: 20px; }
  .wave { position: absolute; inset: 0; }
  .identity {
    position: absolute;
    right: 40px; top: 42px;
    text-align: right;
  }
  .identity__name {
    font-family: "Arvo", Georgia, serif;
    font-weight: 700;
    font-size: 24px;
    letter-spacing: .5px;
    color: var(--brand-red);
    text-transform: uppercase;
  }
  .identity__title {
    font-size: 16px;
    color: var(--white);
    margin-top: 2px;
  }
  .contact {
    position: absolute;
    right: 36px; top: 176px;
    list-style: none;
    color: var(--white);
    font-size: 15px;
    line-height: 25px;
    text-align: right;
  }
  .contact li { display: flex; justify-content: flex-end; align-items: center; gap: 10px; }
  .contact b { font-weight: 700; }
  .contact svg { width: 15px; height: 15px; flex: none; }
  .address {
    position: absolute;
    right: 36px; bottom: 34px;
    color: var(--white);
    font-size: 16px;
  }
</style>
</head>
<body>

  <section class="card card--back" aria-label="Card back">
    <div class="brand-mark"><span class="brand-dot"></span>Plumtarvessa</div>
  </section>

  <section class="card card--front" aria-label="Card front">
    <svg class="wave" viewBox="0 0 700 400" preserveAspectRatio="none" aria-hidden="true">
      <path d="M0,286 C170,284 290,264 380,200 C460,146 560,128 700,122 L700,400 L0,400 Z" fill="var(--steel-dark)"/>
      <path d="M0,294 C170,292 290,272 380,208 C460,154 560,136 700,130 L700,400 L0,400 Z" fill="var(--card-black)"/>
      <path d="M0,301 C170,299 290,279 380,215 C460,161 560,143 700,137 L700,400 L0,400 Z" fill="var(--deep-red)"/>
    </svg>

    <div class="brand-mark"><span class="brand-dot"></span>Plumtarvessa</div>

    <div class="identity">
      <div class="identity__name">Marlo Venturi</div>
      <div class="identity__title">Sales Manager</div>
    </div>

    <ul class="contact">
      <li><span>(555)201-7348 <b>(cell)</b></span>
        <svg viewBox="0 0 16 16" fill="none" stroke="#fff" stroke-width="1.6"><rect x="4" y="1" width="8" height="14" rx="1.5"/><line x1="7" y1="12.5" x2="9" y2="12.5"/></svg></li>
      <li><span>(555)203-6190 <b>(Office)</b></span>
        <svg viewBox="0 0 16 16" fill="#fff"><path d="M3.5 1.5l2.5 3-1.5 1.5c.8 2 2.5 3.7 4.5 4.5l1.5-1.5 3 2.5-1.8 2.3C6.5 13.5 2.5 9.5 1.2 3.3z"/></svg></li>
      <li><span>(555)204-2271</span>
        <svg viewBox="0 0 16 16" fill="#fff"><rect x="4" y="1" width="8" height="5"/><rect x="1" y="6" width="14" height="7" rx="1"/><rect x="4" y="10" width="8" height="5" fill="#d9000d" stroke="#fff"/></svg></li>
      <li><span>Marlo@Plumtarvessa.com</span>
        <svg viewBox="0 0 16 16" fill="none" stroke="#fff" stroke-width="1.6"><rect x="1" y="3" width="14" height="10"/><path d="M1 3l7 6 7-6"/></svg></li>
      <li><span>www.Plumtarvessa.com</span>
        <svg viewBox="0 0 16 16" fill="none" stroke="#fff" stroke-width="1.3"><circle cx="8" cy="8" r="6.5"/><ellipse cx="8" cy="8" rx="3" ry="6.5"/><line x1="1.5" y1="8" x2="14.5" y2="8"/></svg></li>
    </ul>

    <p class="address">482 Alder Crest Way Suite 7 Lakemont, FL 33199</p>
  </section>

</body>
</html>
```